Post Lockdown Ortho Special

We are running a special for (Ortho) Braces/Clear Aligner (Quorvelina), till July 31st 2020. Up to $2,000 off with free Consultation and Xrays.

We need a ad to run in different formats.

Maybe something with: what better time to get braces when you have to wear a mask all the time.

Trying to rebuild our business and get people in for free consultations.

```html
<!DOCTYPE html>
<html lang="en">
<head>
<meta charset="utf-8">
<title>Cedarvale Ortho Special – Ad Set Proposal</title>
<link rel="stylesheet" href="https://fonts.googleapis.com/css2?family=Cinzel:wght@400;700&family=Montserrat:wght@400;600&display=swap">
<style>
  :root{
    --board:#555555;
    --paper:#ffffff;
    --purple:#774ea4;
    --pink:#fbd9e3;
    --ink:#4a4a4a;
    --rule:#c9b6de;
    --label:#f2f2f2;
  }
  *{box-sizing:border-box;margin:0;padding:0}
  html,body{width:1200px;height:902px;overflow:hidden;background:var(--board)}
  .board{position:relative;width:1200px;height:902px;font-family:"Cinzel",serif}
  .format-label{position:absolute;color:var(--label);font-family:"Cinzel",serif;font-size:15px;letter-spacing:.3px;white-space:nowrap}
  .ad{position:absolute;background:var(--paper);overflow:hidden}
  .ad > *{position:absolute}
  .tooth{border-radius:42% 42% 34% 34% / 30% 30% 50% 50%;background:linear-gradient(180deg,var(--purple) 0%,var(--purple) 28%,#b58fcb 62%,var(--pink) 100%)}
  .headline{color:var(--purple);font-weight:700;white-space:nowrap}
  .body-copy{color:var(--ink);white-space:nowrap}
  .btn{background:var(--purple);color:#fff;font-weight:700;display:flex;align-items:center;justify-content:center;white-space:nowrap}
  .brand{display:flex;align-items:center;gap:5px;color:var(--purple);font-weight:700;white-space:nowrap}
  .brand-dot{border-radius:50%;background:var(--purple);flex:none}
  .rule{height:1px;background:var(--rule)}

  /* skyscraper */
  .sky{left:73px;top:119px;width:181px;height:677px}
  .sky .tooth{left:43px;top:61px;width:98px;height:144px}
  .sky .headline{left:0;width:100%;top:233px;text-align:center;font-size:18px;line-height:24px}
  .sky .body-copy{left:0;width:100%;top:312px;text-align:center;font-size:13.5px;line-height:19px;font-weight:400}
  .sky .rule.top{left:27px;top:405px;width:122px}
  .sky .offer{left:0;width:100%;top:414px;text-align:center;color:var(--ink);font-weight:700}
  .sky .offer small{display:block;font-size:13px;line-height:18px}
  .sky .offer strong{display:block;font-size:19px;line-height:26px}
  .sky .rule.bottom{left:27px;top:467px;width:122px}
  .sky .btn{left:40px;top:501px;width:101px;height:24px;font-size:14px}
  .sky .brand{left:26px;top:600px;font-size:15px}
  .sky .brand-dot{width:26px;height:26px}

  /* leaderboard */
  .leader{left:326px;top:134px;width:674px;height:113px}
  .leader .brand{left:16px;top:46px;font-size:13px}
  .leader .brand-dot{width:22px;height:22px}
  .leader .divider{left:154px;top:10px;width:1px;height:88px;background:var(--purple)}
  .leader .tooth{left:181px;top:16px;width:61px;height:88px}
  .leader .headline{left:274px;top:20px;font-size:18px}
  .leader .body-copy{left:274px;top:43px;font-size:11px;letter-spacing:.9px;font-weight:700}
  .leader .btn{left:274px;top:71px;width:92px;height:22px;font-size:12px}

  /* square pair */
  .sq-a{left:326px;top:363px;width:232px;height:235px}
  .sq-a .tooth{left:64px;top:19px;width:106px;height:150px}
  .sq-a .brand{left:72px;top:193px;font-size:11px}
  .sq-a .brand-dot{width:18px;height:18px}
  .sq-b{left:582px;top:366px;width:233px;height:232px;background:var(--purple)}
  .sq-b .headline{left:0;width:100%;top:68px;text-align:center;color:#fff;font-size:17px;line-height:26px}
  .sq-b .body-copy{left:0;width:100%;top:124px;text-align:center;color:#fff;font-size:12px;line-height:20px}

  /* large rectangle */
  .rect{left:871px;top:363px;width:284px;height:224px}
  .rect .brand{left:167px;top:17px;font-size:10px}
  .rect .brand-dot{width:16px;height:16px}
  .rect .tooth{left:11px;top:47px;width:81px;height:116px}
  .rect .headline{left:110px;top:72px;font-size:14.5px;line-height:18.5px}
  .rect .body-copy{left:110px;top:111px;font-size:9.5px;line-height:17px;font-weight:700}
  .rect .btn{left:112px;top:169px;width:91px;height:22px;font-size:12px}

  /* proposal notes */
  .notes{position:absolute;left:765px;top:694px;color:var(--label);font-family:"Montserrat",sans-serif;font-size:16.5px;line-height:20px;white-space:nowrap}
  .notes b{font-weight:600}
  .notes .gap{height:20px}
</style>
</head>
<body>
<main class="board">

  <p class="format-label" style="left:70px;top:89px">Skyscrapper Ad (Web)</p>
  <section class="ad sky">
    <div class="tooth" role="img" aria-label="Tooth with braces illustration"></div>
    <h2 class="headline">WHAT BETTER<br>TIME TO<br>GET BRACES</h2>
    <p class="body-copy">WHEN YOU HAVE<br>TO WEAR A MASK<br>ALL THE TIME.</p>
    <div class="rule top"></div>
    <p class="offer"><small>Up To</small><strong>$2,000 Off</strong></p>
    <div class="rule bottom"></div>
    <a class="btn">Book Now</a>
    <div class="brand"><span class="brand-dot"></span>Cedarvale</div>
  </section>

  <p class="format-label" style="left:324px;top:89px">Leaderboard Ad (Web)</p>
  <section class="ad leader">
    <div class="brand"><span class="brand-dot"></span>Cedarvale</div>
    <div class="divider"></div>
    <div class="tooth" role="img" aria-label="Tooth with braces illustration"></div>
    <h2 class="headline">WHAT BETTER TIME TO GET BRACES</h2>
    <p class="body-copy">WHEN YOU HAVE TO WEAR A MASK ALL THE TIME.</p>
    <a class="btn">Book Now</a>
  </section>

  <p class="format-label" style="left:323px;top:327px">Square Animated /Pictora/ Circlebook Ad</p>
  <section class="ad sq-a">
    <div class="tooth" role="img" aria-label="Tooth with braces illustration"></div>
    <div class="brand"><span class="brand-dot"></span>Cedarvale</div>
  </section>
  <section class="ad sq-b">
    <h2 class="headline">WHAT BETTER TIME<br>TO GET BRACES</h2>
    <p class="body-copy">WHEN YOU HAVE TO WEAR<br>A MASK ALL THE TIME.</p>
  </section>

  <p class="format-label" style="left:875px;top:327px">Large Rectangle Ad</p>
  <section class="ad rect">
    <div class="brand"><span class="brand-dot"></span>Cedarvale</div>
    <div class="tooth" role="img" aria-label="Tooth with braces illustration"></div>
    <h2 class="headline">WHAT BETTER TIME<br>TO GET BRACES</h2>
    <p class="body-copy">WHEN YOU HAVE TO WEAR<br>A MASK ALL THE TIME.</p>
    <a class="btn">Book Now</a>
  </section>

  <div class="notes">
    <p><b>Design Proposal:</b> Cedarvale Advertisement</p>
    <div class="gap"></div>
    <p><b>Files included in package:</b></p>
    <p>•Working file (Vectorine Studio)</p>
    <p>•Image File/Gif (Ad format)</p>
  </div>

</main>
</body>
</html>
```